Prestige Car Bodyshop Business Card

We are a car bodyshop based in the UK. Our customer base is mainly prestige high-value vehicles. I am looking for a classy and stylish business card design for my staff to give out to customers, with their direct email and phone number, as well as our main email and phone number with address details

I am also looking to have a general business card design with just our main company address and contact details, but also have a space to add a manufacturer approval logo (i.e Velmora, Orek, Tovalo etc... logo) in the corner somewhere.

I do not particularly want any outlines or pictures of cars on the card, I would just like a quality high-end look.

Please feel free to get in touch if you have any questions or queries?

Many Thanks

Malcolm

Target Market(s)

Prestige vehicle owners

Industry/Entity Type

Automotive

Contact Information for Business Card

I am looking for a classy and stylish business card design for my staff to give out to customers, with their direct email and phone number, as well as our main email and phone number with address details

Font styles to use
Sans Serif

Colors

Designer to choose colors to be used in the design.

Requirements
Nice to have
• I do not particularly want any outlines or pictures of cars on the card, I would just like a quality high-end look.

```html
<!DOCTYPE html>
<html lang="en">
<head>
<meta charset="utf-8">
<title>Halden Accident Repair Centre – Business Cards</title>
<link href="https://fonts.googleapis.com/css2?family=Source+Sans+3:wght@300;400&display=swap" rel="stylesheet">
<style>
  :root {
    --backdrop: #e9e6e1;
    --card-white: #f7f7f5;
    --navy: #13306a;
    --navy-deep: #11285a;
    --brand-blue: #1d4f9c;
    --ink: #1f2433;
    --silver: #d9d5cb;
    --gold: #b9a47a;
  }
  * { margin: 0; padding: 0; box-sizing: border-box; }
  html, body { width: 1200px; height: 1200px; overflow: hidden; }
  body {
    background: var(--backdrop);
    font-family: "Source Sans 3", sans-serif;
    position: relative;
  }
  .card {
    position: absolute;
    left: 340px;
    width: 520px;
    height: 324px;
    box-shadow: 0 6px 18px rgba(0,0,0,0.12);
  }
  .card--front { top: 226px; background: var(--card-white); }
  .card--back { top: 667px; background: var(--navy-deep); }

  .brand { position: absolute; display: flex; align-items: center; }
  .brand__mark { border-radius: 50%; flex: none; }
  .brand__text { font-weight: 300; line-height: 1; }
  .brand__name { letter-spacing: 0.01em; }
  .brand__tagline { letter-spacing: 0.04em; margin-top: 8px; }

  .card--front .brand { left: 38px; top: 126px; }
  .card--front .brand__mark { width: 72px; height: 72px; background: var(--brand-blue); margin-right: 12px; }
  .card--front .brand__text { color: var(--brand-blue); }
  .card--front .brand__name { font-size: 30px; }
  .card--front .brand__tagline { font-size: 10.5px; }

  .card--back .brand { left: 85px; top: 105px; }
  .card--back .brand__mark { width: 116px; height: 116px; background: var(--silver); margin-right: 20px; }
  .card--back .brand__text { color: var(--gold); }
  .card--back .brand__name { font-size: 46px; }
  .card--back .brand__tagline { font-size: 15px; margin-top: 12px; }

  .divider {
    position: absolute; left: 277px; top: 80px;
    width: 2px; height: 164px; background: var(--navy);
  }
  .contact { position: absolute; left: 296px; top: 92px; color: var(--ink); }
  .contact__name { font-size: 20px; line-height: 1.1; }
  .contact__title { font-size: 13.5px; margin-top: 2px; }
  .contact__list { list-style: none; margin-top: 18px; font-size: 13.5px; }
  .contact__item { display: flex; align-items: flex-start; margin-bottom: 9px; line-height: 1.2; }
  .contact__item svg { width: 13px; height: 13px; margin-right: 5px; margin-top: 2px; flex: none; fill: var(--navy); }
</style>
</head>
<body>

  <section class="card card--front">
    <div class="brand">
      <div class="brand__mark"></div>
      <div class="brand__text">
        <div class="brand__name">HALDEN</div>
        <div class="brand__tagline">ACCIDENT REPAIR CENTRE</div>
      </div>
    </div>

    <div class="divider"></div>

    <div class="contact">
      <div class="contact__name">Your Name</div>
      <div class="contact__title">Job title</div>
      <ul class="contact__list">
        <li class="contact__item">
          <svg viewBox="0 0 16 16"><path d="M1 6c0-2 3-3 7-3s7 1 7 3v1h-4V5.5H5V7H1z"/><path d="M3 8h10l1 5H2z"/></svg>
          000 000 0000
        </li>
        <li class="contact__item">
          <svg viewBox="0 0 16 16"><path d="M1 4h14v9H1z M2 5l6 4.5L14 5" fill="none" stroke="#13306a" stroke-width="1.4"/><path d="M1 4h14L8 9z"/></svg>
          youremail@xyz.com
        </li>
        <li class="contact__item">
          <svg viewBox="0 0 16 16"><path d="M8 1a5 5 0 0 1 5 5c0 4-5 9-5 9S3 10 3 6a5 5 0 0 1 5-5zm0 3a2 2 0 1 0 0 4 2 2 0 0 0 0-4z"/></svg>
          <span>0000, Any street, Anywhere<br>Province name 00000</span>
        </li>
      </ul>
    </div>
  </section>

  <section class="card card--back">
    <div class="brand">
      <div class="brand__mark"></div>
      <div class="brand__text">
        <div class="brand__name">HALDEN</div>
        <div class="brand__tagline">ACCIDENT REPAIR CENTRE</div>
      </div>
    </div>
  </section>

</body>
</html>
```